Business Card Design. For a portrait and wedding photography business

Silver Willow Studio Weddings, Portraits, Bar/Bat Mitzvah, Sweet 16's, On the Cutting Edge of Digital Photography Corporate Events High Quality Photography at an Affordable PricesCustom Wedding Packages.Custom Designed Album, Thank you cardsExpert Photo Editing and Retouching

Target Market(s)

Families for family portraits, head shots for business cards,, wedding clients, Suite 16's, bar/bat mitzvah, parties, and corporate events,
.

Industry/Entity Type

Wedding

Contact Information for Business Card

Daniel K. Fenwick 47 Larchmere Lane Cornwall, N.Y. 14306 By Appointment Only

Font styles to use
Script
Other font styles liked:
• Time New Romen

Requirements
Must have
• I would like to use one of the photograph I uploaded I would prefer to let the designer choose based on their expertise.
Nice to have
• Leave it up to the designer
Should not have
• The card should not be too dark

```html
<!DOCTYPE html>
<html lang="en">
<head>
<meta charset="utf-8">
<title>Daniel K. Fenwick – Business Card</title>
<link rel="stylesheet" href="https://fonts.googleapis.com/css2?family=Gentium+Book+Plus:wght@400;700&display=swap">
<style>
  :root {
    --backdrop: #222222;
    --card: #f6f6f5;
    --ink: #1e1e1e;
    --accent-red: #b3141c;
    --band: #0b0b0b;
    --photo-dark: #141210;
    --photo-mid: #6d665d;
    --photo-light: #d9d3c8;
  }
  html, body {
    margin: 0;
    padding: 0;
    width: 1200px;
    height: 900px;
    overflow: hidden;
    background: var(--backdrop);
  }
  .stage {
    position: relative;
    width: 1200px;
    height: 900px;
  }
  .business-card {
    position: absolute;
    left: 100px;
    top: 164px;
    width: 1000px;
    height: 572px;
    background: var(--card);
    border-radius: 20px;
    overflow: hidden;
    font-family: "Gentium Book Plus", "Times New Roman", serif;
  }
  .photo-drops {
    position: absolute;
    inset: 0;
  }
  .contact {
    position: absolute;
    left: 72px;
    top: 318px;
  }
  .contact__name {
    margin: 0 0 22px;
    font-size: 42px;
    font-weight: 400;
    color: var(--accent-red);
    letter-spacing: 0.01em;
  }
  .contact__address {
    margin: 0;
    font-style: normal;
    font-size: 23px;
    line-height: 1.5;
    color: var(--ink);
  }
  .appointment-band {
    position: absolute;
    left: 0;
    right: 0;
    bottom: 0;
    height: 78px;
    background: var(--band);
    display: flex;
    align-items: center;
    justify-content: center;
  }
  .appointment-band__text {
    margin: 0;
    font-size: 21px;
    letter-spacing: 0.62em;
    text-transform: uppercase;
    color: var(--accent-red);
  }
</style>
</head>
<body>
<main class="stage">
  <section class="business-card">
    <svg class="photo-drops" width="1000" height="572" viewBox="0 0 1000 572">
      <defs>
        <linearGradient id="portrait-mono" x1="0" y1="0" x2="1" y2="1">
          <stop offset="0" stop-color="#2b2b2b"/>
          <stop offset="0.5" stop-color="#9a9a9a"/>
          <stop offset="1" stop-color="#3a3a3a"/>
        </linearGradient>
        <radialGradient id="portrait-sepia" cx="0.45" cy="0.55" r="0.6">
          <stop offset="0" stop-color="var(--photo-light)"/>
          <stop offset="0.45" stop-color="var(--photo-mid)"/>
          <stop offset="1" stop-color="var(--photo-dark)"/>
        </radialGradient>
      </defs>
      <path class="photo-drops__small"
            role="img" aria-label="Black and white photograph of a wedding couple kissing outdoors"
            d="M556,50 C520,70 500,95 476,108 A82 82 0 1 0 497,203 C510,170 525,95 556,50 Z"
            fill="url(#portrait-mono)" stroke="var(--accent-red)" stroke-width="5" stroke-linejoin="round"/>
      <path class="photo-drops__large"
            role="img" aria-label="Warm toned photograph of a groom embracing his bride in her lace gown"
            d="M548,488 C546,440 570,395 585,353 C580,340 574,328 571,315 A190 190 0 1 1 717,437 C657,427 590,450 548,488 Z"
            fill="url(#portrait-sepia)" stroke="var(--accent-red)" stroke-width="5" stroke-linejoin="round"/>
    </svg>

    <div class="contact">
      <h1 class="contact__name">Daniel K. Fenwick</h1>
      <address class="contact__address">47 Larchmere Lane Cornwall,<br>N.Y. 14306</address>
    </div>

    <footer class="appointment-band">
      <p class="appointment-band__text">By Appointment Only</p>
    </footer>
  </section>
</main>
</body>
</html>
```